Used Car Business Card Design

Maple Ridge Auto Sales is a woman owned women friendly car lot.  We focus on providing Professionalism, Integrity and Respect beginning with the initial introduction.  We place the highest importance on customer service after the sale and our rating with the Fair Trade Bureau of Arkansas shows it.  We're starting out 7th year, recently relocated. Satisfied Clients bring their family members, friends and co-workers to buy their cars, SUV's and trucks from MRAS.
You buy here / you pay here, Lending program opportunities too, Great Cash Prices
Finance with Flexibility we look at each individual uniquely and not a credit score
I think of my kids when getting our vehicles ready and your safety when you drive away in a MRAS car. . .  Drive away with Peace of Mind...
Maroon, Black and Silver colors.

Updates
I sent a response to the designers - have  not heard from them, will I receive my funds back?

Thank you all,  a lot of great designs - Making my decision on Nov 4th

So much talent. . .
So very challenging. . .
Thank you for your participation.
Sincerely,
Maple Ridge Auto Sales
Lorna Pettigrew

Industry/Entity Type
Safety
Contact Information for Business Card
Maple Ridge Auto Sales
"A Solid Car for a Solid Price"
4153 Oakvale Rd. North Ridgeview, Ar 72990
Lorna Pettigrew
501.739.2018

```html
<!DOCTYPE html>
<html lang="en">
<head>
<meta charset="utf-8">
<title>Maple Ridge Auto Sales – Business Card</title>
<link rel="stylesheet" href="https://fonts.googleapis.com/css2?family=Aladin&family=Russo+One&family=PT+Sans:wght@700&family=Michroma&family=Arimo:wght@700&display=swap">
<style>
  :root {
    --maroon: #b5161c;
    --maroon-deep: #8e0d12;
    --maroon-light: #d23a3a;
    --band-light: #f6e4e4;
    --silver: #d9d9d9;
    --ink: #222222;
    --tagline: #5a1414;
    --white: #ffffff;
    --sheet: #ffffff;
    --frame: #e2e2e2;
  }
  * { margin: 0; padding: 0; box-sizing: border-box; }
  html, body { width: 1200px; height: 465px; overflow: hidden; background: var(--sheet); }
  .sheet {
    position: relative; width: 1200px; height: 465px;
    border: 1px solid var(--frame); background: var(--sheet);
  }
  .side-label {
    position: absolute; top: 10px; width: 560px; text-align: center;
    font-family: "Aladin", serif; font-weight: 400; font-size: 46px; line-height: 52px; color: var(--ink);
  }
  .side-label--front { left: 30px; }
  .side-label--rear { left: 611px; }

  .card {
    position: absolute; top: 72px; width: 560px; height: 347px; overflow: hidden;
    background: linear-gradient(180deg, var(--maroon-light) 0%, var(--maroon) 45%, var(--maroon-deep) 100%);
    box-shadow: 0 8px 10px -6px rgba(0,0,0,0.35);
  }
  .card--front { left: 30px; }
  .card--rear { left: 611px; }

  .card__photo {
    position: absolute; inset: 0;
    background:
      radial-gradient(ellipse 45% 35% at 20% 70%, rgba(60,0,0,0.35), transparent 70%),
      radial-gradient(ellipse 60% 40% at 75% 45%, rgba(255,120,120,0.25), transparent 70%),
      radial-gradient(ellipse 30% 25% at 85% 80%, rgba(60,0,0,0.3), transparent 70%);
  }

  .card__header {
    position: absolute; left: 0; top: 0; width: 100%;
    background: linear-gradient(90deg, var(--band-light) 0%, var(--white) 50%, var(--band-light) 100%);
    text-align: center;
  }
  .card--front .card__header { height: 73px; padding-top: 6px; }
  .card--rear .card__header { background: transparent; padding-top: 24px; }
  .brand-name {
    font-family: "Russo One", sans-serif; font-weight: 400; color: var(--ink);
    letter-spacing: 3px; line-height: 1.1; white-space: nowrap;
  }
  .card--front .brand-name { font-size: 27px; }
  .card--rear .brand-name { font-size: 33px; color: var(--silver); }
  .tagline {
    font-family: "Arimo", sans-serif; font-weight: 700; line-height: 1.2; white-space: nowrap;
  }
  .card--front .tagline { font-size: 22px; color: var(--tagline); margin-top: 2px; }
  .card--rear .tagline { font-size: 27px; color: var(--white); margin-top: 4px; text-shadow: 1px 1px 2px rgba(0,0,0,0.6); }

  .selling-points {
    position: absolute; left: 0; top: 89px; width: 100%; text-align: center; list-style: none;
    font-family: "PT Sans", sans-serif; font-weight: 700; font-size: 33px; line-height: 39px;
    color: var(--white); text-shadow: 2px 2px 3px rgba(0,0,0,0.7); white-space: nowrap;
  }

  .contact-strip {
    position: absolute; left: 0; top: 119px; width: 350px; height: 24px;
    background: linear-gradient(90deg, var(--white) 0%, var(--white) 60%, rgba(255,255,255,0));
    font-family: "Arimo", sans-serif; font-weight: 700; font-size: 15px; line-height: 16px; color: var(--ink);
    padding: 4px 0 0 14px; white-space: nowrap;
  }
  .contact-details {
    position: absolute; left: 0; top: 174px; width: 100%; text-align: center; font-style: normal;
    font-family: "PT Sans", sans-serif; font-weight: 700; font-size: 27px; line-height: 28.5px;
    color: var(--white); letter-spacing: 0.5px; white-space: nowrap;
    text-shadow: -1px -1px 0 #3a0a0a, 1px -1px 0 #3a0a0a, -1px 1px 0 #3a0a0a, 1px 1px 0 #3a0a0a, 2px 2px 3px rgba(0,0,0,0.6);
  }

  .card__footer {
    position: absolute; left: 0; bottom: 0; width: 100%; height: 34px;
    background: linear-gradient(90deg, var(--band-light) 0%, var(--white) 50%, var(--band-light) 100%);
    text-align: center; padding-top: 8px; white-space: nowrap;
    font-family: "Michroma", sans-serif; font-size: 15px; line-height: 18px; letter-spacing: 0.6px; color: var(--white);
    text-shadow: -1px -1px 0 #444, 1px -1px 0 #444, -1px 1px 0 #444, 1px 1px 0 #444;
  }
</style>
</head>
<body>
<main class="sheet">
  <h2 class="side-label side-label--front">Front</h2>
  <h2 class="side-label side-label--rear">Rear</h2>

  <section class="card card--front">
    <div class="card__photo" role="img" aria-label="Faint red-toned photo of a car in the background"></div>
    <header class="card__header">
      <h1 class="brand-name">MAPLE RIDGE AUTO SALES</h1>
      <p class="tagline">"A Solid Car for a Solid Price"</p>
    </header>
    <ul class="selling-points">
      <li>You buy here / you pay here,</li>
      <li>Lending program opportunities too,</li>
      <li>Great Cash Prices</li>
      <li>Drive away with Peace of Mind...</li>
      <li>Maroon, Black and Silver colors.</li>
    </ul>
    <footer class="card__footer">PROFESSIONALISM, INTEGRITY AND RESPECT</footer>
  </section>

  <section class="card card--rear">
    <div class="card__photo" role="img" aria-label="Faint red-toned photo of a car in the background"></div>
    <header class="card__header">
      <h1 class="brand-name">MAPLE RIDGE AUTO SALES</h1>
      <p class="tagline">"A Solid Car for a Solid Price"</p>
    </header>
    <p class="contact-strip">Contact Information for Business Card :</p>
    <address class="contact-details">
      Maple Ridge Auto Sales<br>
      "A Solid Car for a Solid Price"<br>
      4153 Oakvale Rd. North Ridgeview,<br>
      Ar 72990 Lorna Pettigrew 501.739.2018
    </address>
    <footer class="card__footer">PROFESSIONALISM, INTEGRITY AND RESPECT</footer>
  </section>
</main>
</body>
</html>
```